Etiketten-Design für Eierschachtel
Zielgruppe
Wir haben einen Hofladen, indem wir unsere hofeigenen Produkte direkt an den Verbraucher verkaufen.
Aufgabenstellung
Wir suchen ein Etikett für unsere Eierschachtel, die wir für den Verkauf unserer Eier im eigenen Hofladen benötigen.
Das Etikett soll hell und freundlich, aber keinesfalls überladen oder zu verspielt sein. Es soll die Natürlichkeit und Regionalität widerspiegeln. Wir halten unsere Hühner in mobiler Freilandhaltung mit ausreichend Auslauf auf unseren Wiesen.
Das beigefügte Logo (einmal farbig, einmal schwarz/weiß - je nach Vorschlag was besser passt) soll integriert werden.
Das Etikett soll folgende Punkte enthalten:
Rückseite:
- 'Verbraucherhinweis: Nach dem Kauf bei Kühlschranktemperatur aufbewahren. Nach Ablauf des
Mindesthaltbarkeitsdatums durcherhitzen.'
- Familie Haslbeck
Lindenweg 7
84273 Deutenhausen
Vorderseite (zum Öffnen der Eierschachtel) bzw. Deckel oben:
- '10 frische Eier aus mobiler Freilandhaltung' (gerne auch eigene Vorschläge von Ihnen)
- passender Slogan, der auf Regionalität bzw. Einkaufen direkt beim Erzeuger basiert
Format: ca. 21,4cm breit und ca. 14,2cm lang

```html
<!DOCTYPE html>
<html lang="de">
<head>
<meta charset="utf-8">
<title>Haslbeck Hof – Eieretikett</title>
<link rel="stylesheet" href="https://fonts.googleapis.com/css2?family=Open+Sans:wght@400;600;700&display=swap">
<style>
  :root {
    --backdrop: #e9ece4;
    --label-white: #ffffff;
    --farm-green: #3f9a4a;
    --earth-brown: #8a5527;
    --band-text: #ffffff;
    --badge-fill: #f4efe8;
    --badge-text: #7a4a22;
    --meadow-dark: #4f7a35;
    --meadow-light: #9fc56f;
    --hen-brown: #a8652a;
    --bark-grey: #8b8b80;
    --bark-green: #6f8a5c;
  }
  * { margin: 0; padding: 0; box-sizing: border-box; }
  html, body {
    width: 1200px;
    height: 789px;
    overflow: hidden;
    background: var(--backdrop);
    font-family: "Open Sans", Arial, sans-serif;
  }
  .egg-label {
    position: absolute;
    left: 50px;
    top: 185px;
    width: 1100px;
    height: 420px;
    display: flex;
    background: var(--label-white);
    box-shadow: 0 6px 24px rgba(0,0,0,0.08);
  }
  .photo-pasture {
    width: 380px;
    height: 100%;
    background: linear-gradient(160deg, var(--bark-grey) 0%, #a29d90 45%, var(--bark-green) 100%);
  }
  .wrap-panel {
    width: 320px;
    height: 100%;
    position: relative;
    background: var(--label-white);
  }
  .farm-mark {
    position: absolute;
    top: 42px;
    left: 0;
    right: 0;
    display: flex;
    flex-direction: column;
    align-items: center;
    gap: 14px;
  }
  .farm-mark-dot {
    width: 70px;
    height: 70px;
    border-radius: 50%;
    border: 2px solid var(--farm-green);
  }
  .farm-name {
    font-weight: 600;
    font-size: 24px;
    letter-spacing: 2px;
    color: var(--farm-green);
  }
  .claim-band {
    position: absolute;
    left: 0;
    right: 0;
    top: 220px;
    height: 92px;
    background: var(--earth-brown);
    color: var(--band-text);
    display: flex;
    flex-direction: column;
    justify-content: center;
    padding-left: 26px;
  }
  .claim-title {
    font-weight: 700;
    font-size: 29px;
    letter-spacing: 1px;
    line-height: 1.1;
  }
  .claim-sub {
    font-weight: 400;
    font-size: 15px;
    letter-spacing: 1.2px;
    margin-top: 4px;
  }
  .photo-hen {
    flex: 1;
    height: 100%;
    position: relative;
    background:
      radial-gradient(ellipse 45% 55% at 35% 45%, var(--hen-brown) 0%, rgba(168,101,42,0.6) 55%, rgba(168,101,42,0) 100%),
      linear-gradient(135deg, var(--meadow-dark) 0%, var(--meadow-light) 60%, var(--meadow-dark) 100%);
  }
  .count-badge {
    position: absolute;
    right: 36px;
    bottom: 30px;
    width: 118px;
    height: 118px;
    border-radius: 50%;
    background: var(--badge-fill);
    color: var(--badge-text);
    display: flex;
    flex-direction: column;
    align-items: center;
    justify-content: center;
  }
  .count-number {
    font-weight: 700;
    font-size: 44px;
    line-height: 1;
  }
  .count-caption {
    font-weight: 700;
    font-size: 11px;
    letter-spacing: 1px;
    margin-top: 6px;
  }
</style>
</head>
<body>
  <main class="egg-label">
    <div class="photo-pasture" role="img" aria-label="Unscharfes Foto einer Wiese mit Baumstamm"></div>
    <section class="wrap-panel">
      <div class="farm-mark">
        <span class="farm-mark-dot"></span>
        <span class="farm-name">HASLBECK HOF</span>
      </div>
      <div class="claim-band">
        <p class="claim-title">FRISCHE EIER AUS</p>
        <p class="claim-sub">MOBILER FREILANDHALTUNG</p>
      </div>
    </section>
    <div class="photo-hen" role="img" aria-label="Foto eines braunen Huhns auf einer grünen Wiese">
      <div class="count-badge">
        <span class="count-number">10</span>
        <span class="count-caption">FRISCHE EIER</span>
      </div>
    </div>
  </main>
</body>
</html>
```